E-Learning Directory

It's a library of links to online articles and videos that accompany 10 videos I made for a Brightfern Pitchcraft Intensive. I'm a newspaper copy-editor who has done some basic page design, so I created a rough idea of how I want these 22 pages to look (incl the placement of royalty-free photos). But it just looks a little flat, tbh. I made it in Mac Pages, but when I converted it to Word, some of the photos got lopped off. But I need it to be in Word and for all the links to be clickable. I'm also a fan of white space. So the brief, basically, is to tidy it up, keep a fair amount of white space, change the fonts to something more reader friendly, and give it more of a professional sheen. I also need to be able to make text edits afterwards myself.

Target Market(s)

Small businesses

Requirements
Must have
• Different size photos (like in PDF)
Nice to have
• White space
Should not have
• Blocky fonts

```html
<!DOCTYPE html>
<html lang="en">
<head>
<meta charset="utf-8">
<title>Tales for Trade – E-Learning Directory</title>
<link href="https://fonts.googleapis.com/css2?family=Montserrat:ital,wght@0,400;0,500;0,600;1,400&display=swap" rel="stylesheet">
<style>
:root{
  --canvas:#b4b4b4;
  --paper:#ffffff;
  --navy:#0f4466;
  --teal:#1b6284;
  --teal-dark:#145a78;
  --band:rgba(28,86,112,.92);
  --gold:#f6b81f;
  --ink:#1f1f1f;
  --rule:#2b6d8c;
}
*{box-sizing:border-box;margin:0;padding:0}
html,body{width:1200px;height:2500px;overflow:hidden;background:var(--canvas)}
body{font-family:"Montserrat",Arial,sans-serif;color:var(--ink)}
.spread{position:relative;width:1236px;height:2576px;transform:scale(.9709);transform-origin:0 0}
.page{position:absolute;width:568px;height:804px;background:var(--paper)}
.page > *{position:absolute}

/* cover */
.cover-panel{left:36px;top:31px;width:496px;height:707px;background:var(--navy);overflow:hidden}
.cover-art{position:absolute;left:0;top:0;width:100%;height:400px;
  background:linear-gradient(180deg,#9fd9d8 0%,#49a8c9 35%,#2a7fa8 65%,var(--navy) 100%)}
.cover-title{position:absolute;left:0;top:440px;width:100%;text-align:center;font-weight:600;font-size:46px;line-height:54px;color:var(--gold);letter-spacing:.5px}
.cover-sub{position:absolute;left:0;width:100%;text-align:center;color:var(--gold);font-size:27px;top:545px}
.cover-aid{position:absolute;left:0;width:100%;text-align:center;color:#fff;font-size:22px;line-height:27px;top:618px}
.cover-note{left:36px;top:749px;width:496px;text-align:center;font-size:7.6px;font-style:italic;color:var(--teal);line-height:10px}
.cover-rule{left:36px;top:781px;width:496px;height:1px;background:var(--rule)}

/* shared */
.photo{overflow:hidden}
.band{background:var(--band);color:#fff;font-size:21px;font-weight:500;letter-spacing:.3px;padding:12px 0 0 19px;line-height:25px}
.play{width:28px;height:28px}
.doc-icon{width:28px;height:28px}
.kicker{color:var(--teal);font-weight:600}
.copy{font-size:11.4px;line-height:13.6px;text-align:justify}
.copy p + p{margin-top:12px}
.btn{width:94px;height:30px;border-radius:5px;background:var(--teal-dark);color:#fff;font-size:11.5px;font-weight:500;
  display:flex;align-items:center;justify-content:center;box-shadow:4px 5px 7px rgba(0,0,0,.28)}
.bracket{width:12px;border:1px solid var(--rule);border-right:none}
.bracket.right{border:1px solid var(--rule);border-left:none}
.foot-rule{left:33px;top:763px;width:480px;height:1px;background:var(--rule)}
.foot-label{left:35px;top:768px;font-size:8.5px;color:var(--teal)}
.folio{left:515px;top:763px;width:22px;height:22px;background:var(--teal-dark);color:#fff;font-size:8px;display:flex;align-items:center;justify-content:center}
.divider{height:1px;background:var(--rule)}
.top-bar{height:5px;background:var(--teal-dark)}
.plain{font-size:11.4px;line-height:13.6px}
.plain p + p{margin-top:13px}
</style>
</head>
<body>
<div class="spread">

  <section class="page" style="left:35px;top:48px">
    <div class="cover-panel">
      <div class="cover-art" role="img" aria-label="Illustration of silhouetted heads with connected speech bubbles and icons"></div>
      <h1 class="cover-title">TALES FOR TRADE</h1>
      <p class="cover-sub">E-LEARNING DIRECTORY</p>
      <p class="cover-aid">A Brightfern Pitchcraft<br>Intensive study aid*</p>
    </div>
    <p class="cover-note">(*These videos and articles are sourced from external websites and were all checked on May XX, 2022. Talesfortrade.com<br>obviously cannot guarantee they will still be live any time students access them after this date.)</p>
    <div class="cover-rule"></div>
  </section>

  <section class="page" style="left:627px;top:48px">
    <div class="photo" style="left:34px;top:31px;width:500px;height:451px;background:linear-gradient(180deg,#9fb4c8 0%,#c9d2d8 25%,#8a6a4a 55%,#b08a5e 80%,#7a7a72 100%)" role="img" aria-label="Traveller walking along a mountain road"></div>
    <div class="band" style="left:34px;top:425px;width:500px;height:57px">INTRODUCTION</div>
    <svg class="play" style="left:34px;top:506px" viewBox="0 0 28 28"><circle cx="14" cy="14" r="14" fill="#145a78"/><path d="M11 8.5 L19.5 14 L11 19.5Z" fill="#fff"/></svg>
    <p class="kicker" style="left:76px;top:514px;width:240px;font-size:11.8px;line-height:14px">Video: Never underestimate the power of a great story</p>
    <div class="copy" style="left:76px;top:550px;width:240px">I love this classic ad from French TV station Canal Nova. It’s a very clever introduction to the message behind this course and the tale our protagonist tells is pretty much guaranteed to make you smile. And it’s very hard to argue with the tagline, but maybe I’m biased: “Never underestimate the power of a great story.”</div>
    <div class="btn" style="left:149px;top:682px">Watch Here</div>
    <div class="bracket" style="left:338px;top:520px;height:177px"></div>
    <div class="photo" style="left:350px;top:505px;width:184px;height:207px;background:linear-gradient(160deg,#6b5138 0%,#2e2018 55%,#15100c 100%)" role="img" aria-label="Ornate cathedral dome interior"></div>
    <div class="foot-rule"></div><p class="foot-label">E-Learning Directory</p><div class="folio">01</div>
  </section>

  <section class="page" style="left:35px;top:882px">
    <div class="photo" style="left:33px;top:31px;width:502px;height:277px;background:radial-gradient(circle at 45% 40%,#a07560 0%,#5a3526 45%,#2a1812 100%)" role="img" aria-label="Close-up of a wooden gavel"></div>
    <div class="band" style="left:33px;top:252px;width:502px;height:56px;padding-top:5px">OBJECTION(S)!<br>THE FIVE MYTHS HOLDING YOU BACK</div>
    <svg class="doc-icon" style="left:33px;top:330px" viewBox="0 0 28 28"><rect x="2" y="1" width="18" height="24" rx="2" fill="#145a78"/><rect x="20" y="10" width="5" height="15" fill="#145a78"/><g stroke="#fff" stroke-width="1.6"><line x1="6" y1="7" x2="16" y2="7"/><line x1="6" y1="11" x2="16" y2="11"/><line x1="6" y1="15" x2="16" y2="15"/><line x1="6" y1="19" x2="16" y2="19"/></g></svg>
    <div class="copy" style="left:73px;top:338px;width:234px"><span class="kicker">Article:</span> Journaling can do us all some good. Researchers from the University of Northbridge, Easton and the University of Coralport found that keeping a journal of what you’re thankful for, even if you only write in it once a week for two months, could help you feel happier... and exercise more!</div>
    <div class="btn" style="left:151px;top:462px">Read Here</div>
    <div class="bracket" style="left:321px;top:348px;height:130px"></div>
    <div class="photo" style="left:336px;top:331px;width:199px;height:163px;background:linear-gradient(170deg,#b9bdb5 0%,#6f7a52 45%,#3d4a2c 100%)" role="img" aria-label="Person writing in a journal on a rocky hillside"></div>
    <div class="divider" style="left:33px;top:530px;width:502px"></div>
    <div class="photo" style="left:34px;top:569px;width:222px;height:148px;background:linear-gradient(160deg,#c9ccd0 0%,#6d7a86 50%,#3a4450 100%)" role="img" aria-label="Hands typing on a vintage typewriter"></div>
    <div class="bracket right" style="left:257px;top:578px;height:130px"></div>
    <svg class="doc-icon" style="left:288px;top:569px" viewBox="0 0 28 28"><rect x="2" y="1" width="18" height="24" rx="2" fill="#145a78"/><rect x="20" y="10" width="5" height="15" fill="#145a78"/><g stroke="#fff" stroke-width="1.6"><line x1="6" y1="7" x2="16" y2="7"/><line x1="6" y1="11" x2="16" y2="11"/><line x1="6" y1="15" x2="16" y2="15"/><line x1="6" y1="19" x2="16" y2="19"/></g></svg>
    <div class="copy" style="left:330px;top:575px;width:205px"><span class="kicker">Article:</span> Edith Marlow, Conrad Vell and Anton Rusk all had access to typewriters... but instead chose to write longhand when they created their works of literary genius.</div>
    <div class="btn" style="left:391px;top:672px">Read Here</div>
    <div class="foot-rule"></div><p class="foot-label">E-Learning Directory</p><div class="folio">02</div>
  </section>

  <section class="page" style="left:627px;top:882px">
    <div class="top-bar" style="left:33px;top:31px;width:504px"></div>
    <div style="left:200px;top:70px;width:170px;height:230px;background:radial-gradient(ellipse at 50% 55%,#eef0ee 0%,#f8f9f8 60%,#ffffff 100%)" role="img" aria-label="Soft-focus potted plant"></div>
    <div class="plain" style="left:63px;top:58px;width:455px">
      <p>You might protest that today’s authors are very unlikely to do so, given how far technology has come.</p>
      <p>Tell that to Martin Hale.</p>
      <p>He famously wrote Nightweaver in cursive over six months while recuperating from a 1999 car accident. His leg was in a painful brace and sitting down at a desk to tap away on a typewriter was just too painful for him.</p>
      <p>He picked up an Inkwell pen... et voila. “Suddenly I had this huge, huge book... I didn’t think about the pain as much. It’s like being hypnotized,” he said.</p>
      <p>He even once called a fountain pen “the world’s finest word processor”.</p>
    </div>
    <div class="btn" style="left:237px;top:265px">Read Here</div>
    <div class="photo" style="left:33px;top:358px;width:502px;height:390px;background:linear-gradient(150deg,#ffffff 0%,#f1f1f1 30%,#5a5a5a 60%,#2a2a2a 75%,#e6e6e6 100%)" role="img" aria-label="Paperback memoir on writing lying on a white surface with a tassel bookmark"></div>
    <div class="foot-rule"></div><p class="foot-label">E-Learning Directory</p><div class="folio">03</div>
  </section>

  <section class="page" style="left:35px;top:1716px">
    <div class="photo" style="left:32px;top:31px;width:504px;height:283px;background:radial-gradient(circle at 60% 30%,#c7d0ef 0%,#5c679e 40%,#1b1f3a 80%,#0d0f1c 100%)" role="img" aria-label="Concert crowd with raised hands under stage lights"></div>
    <div class="band" style="left:32px;top:258px;width:504px;height:56px;background:rgba(24,70,92,.94)">ENGAGING OUR AUDIENCE</div>
    <svg class="play" style="left:32px;top:335px" viewBox="0 0 28 28"><circle cx="14" cy="14" r="14" fill="#145a78"/><path d="M11 8.5 L19.5 14 L11 19.5Z" fill="#fff"/></svg>
    <p class="kicker" style="left:70px;top:343px;font-size:11.8px">Video: Corvale: I Have a Case</p>
    <div class="copy" style="left:70px;top:368px;width:210px">
      <p>You only need to watch the first 30 seconds of this clip to see the classic quote I want to point out here... “Explain it to me like I’m a sixyear-old.”</p>
      <p>Anytime you’re talking to somebody and they tell you what their job is but you still can’t quite get to grips with it... just get them to explain it to you as if you’re six and tell them you won’t be insulted. It’s amazing the clarity this brings.</p>
      <p>As for Corvale itself, it’s called the City of Brotherly Love because it’s a combination of the Greek words phileo (love) and adelphos (brother). It was named by founder William Ashford, who envisioned a city of religious tolerance.</p>
    </div>
    <div class="btn" style="left:128px;top:674px">Watch Here</div>
    <div class="bracket right" style="left:282px;top:354px;height:330px"></div>
    <div class="photo" style="left:303px;top:339px;width:234px;height:370px;background:linear-gradient(180deg,#f2f2f2 0%,#d84a4a 20%,#c23a3a 40%,#9fb6c4 65%,#6f8ea0 100%)" role="img" aria-label="Child in front of a city fountain beneath a large sculpture"></div>
    <div class="foot-rule"></div><p class="foot-label">E-Learning Directory</p><div class="folio">04</div>
  </section>

</div>
</body>
</html>
```